Crestline Venture Partners Business Card Redesign Project

CRESTLINE VENTURE PARTNERS
Our company needs to have its business cards redesigned as the current design no longer reflects the business brand or attracts the type of clientele we are seeking.

MUST LOOK
★ Upmarket
★ Reflect Quality
★ Corporate feel
★ Professional
★ Innovative
★ Colourful

MUST PROMOTE
★ Market Leader
★ Knowledge
★ Expertise
★ Experience
★ Solutions
★ Advice

MUST FEEL
★ Classy
★ Elegant
★ Savvy
★ Edgy
★ Upbeat

WHAT WE DO
Crestline Venture Partners provides project management and project controls consultancy services to companies in many industry sectors, within Australia and overseas. My company has developed a business brand through forging strong business relationships within industry. We provide innovative tools, concepts and solutions to management teams to assist them in better plan and managing there project portfolios.

SECTORS OF INDUSTRY WE SERVICE
★Oil & Gas
★Minerals & Metals
★Petrochemical
★Manufacturing
★Building & Construction
★Telecommunications
★Rail
★Civil

BUSINESS CARD DETAILS REQUIRED ON FRONT
Marcus Delane
Business Owner
Tel: 0438519627
Email: marcusdelane@crestlineventurepartners.com
Website: www.crestlineventurepartners.com.au

BUSINESS CARD DETAILS REQUIRED ON BACK
Providing | Knowledge | Expertise | Experience

ATTACHMENTS

Target Market(s)

Oil & Gas I Mining & Resources I Industry in General
Upmarket Clientele
Corporate World

Industry/Entity Type

Industry

Requirements
Must have
• Must be creative and a unique design
The business card must have information on the front and back

```html
<!DOCTYPE html>
<html lang="en">
<head>
<meta charset="utf-8">
<title>Crestline Venture Partners – Business Card Set</title>
<link href="https://fonts.googleapis.com/css2?family=Open+Sans:wght@300;400;600;700&display=swap" rel="stylesheet">
<style>
  :root {
    --brand-red: #ec1c24;
    --ink: #111111;
    --paper: #ffffff;
    --grey-text: #5a5a5a;
    --stage: #3a302b;
    --label: #ffffff;
  }
  * { margin: 0; padding: 0; box-sizing: border-box; }
  html, body { width: 1200px; height: 913px; overflow: hidden; }
  body {
    background: var(--stage);
    font-family: "Open Sans", Arial, sans-serif;
    position: relative;
  }
  .card {
    position: absolute;
    width: 458px;
    height: 262px;
    overflow: hidden;
    box-shadow: 0 3px 8px rgba(0,0,0,0.45);
  }
  .card-shape { position: absolute; inset: 0; width: 100%; height: 100%; }
  .card--front  { left: 105px; top: 143px; }
  .card--back-1 { left: 597px; top: 138px; }
  .card--back-2 { left: 99px;  top: 442px; background: var(--brand-red); }
  .card--back-3 { left: 597px; top: 430px; background: var(--paper); }

  .set-label {
    position: absolute;
    color: var(--label);
    font-size: 31px;
    font-weight: 400;
  }
  .set-label--1 { left: 930px; top: 86px; }
  .set-label--2 { left: 126px; top: 725px; }
  .set-label--3 { left: 965px; top: 721px; }

  /* Front */
  .holder { position: absolute; left: 194px; top: 26px; white-space: nowrap; }
  .holder-name { color: var(--brand-red); font-weight: 700; font-size: 15px; }
  .holder-role { color: #333; font-size: 11px; margin-left: 4px; }
  .contact-list { position: absolute; left: 194px; top: 69px; list-style: none; }
  .contact-list li {
    display: flex; align-items: center; gap: 6px;
    font-size: 11px; color: #333; height: 17.5px;
  }
  .contact-icon { width: 11px; height: 11px; flex: none; }
  .brand-lockup { position: absolute; left: 100px; top: 178px; }
  .brand-name {
    display: flex; align-items: center; gap: 8px;
    font-size: 19px; font-weight: 600; color: var(--ink); white-space: nowrap;
  }
  .brand-dot { width: 14px; height: 14px; border-radius: 50%; background: var(--brand-red); }
  .brand-tagline {
    font-size: 7px; font-weight: 700; color: var(--ink);
    margin-top: 3px; margin-left: 22px; white-space: nowrap;
  }

  /* Backs */
  .back-mark {
    position: absolute; font-weight: 600; font-size: 22px; line-height: 1.15;
    color: var(--ink);
  }
  .values {
    position: absolute; list-style: none; text-align: center;
    font-weight: 300; font-size: 19px; line-height: 32px; color: var(--grey-text);
  }
  .card--back-1 .values { left: 48px; top: 74px; }
  .card--back-1 .back-mark { left: 182px; top: 94px; }
  .card--back-2 .back-mark { left: 70px; top: 94px; color: var(--paper); }
  .card--back-2 .values { left: 228px; top: 70px; color: var(--paper); }
  .card--back-3 .back-mark { left: 82px; top: 94px; }
  .card--back-3 .values { left: 236px; top: 69px; }
</style>
</head>
<body>

<span class="set-label set-label--1">Back 1</span>
<span class="set-label set-label--2">Back 2</span>
<span class="set-label set-label--3">Back 3</span>

<!-- Front -->
<section class="card card--front" aria-label="Card front">
  <svg class="card-shape" viewBox="0 0 458 262" preserveAspectRatio="none" aria-hidden="true">
    <rect width="458" height="262" fill="var(--brand-red)"/>
    <path d="M172,0 C40,40 0,190 92,262 L458,262 L458,0 Z" fill="var(--ink)"/>
    <path d="M200,0 C70,40 25,195 112,262 L458,262 L458,0 Z" fill="var(--paper)"/>
  </svg>
  <p class="holder"><span class="holder-name">MARCUS DELANE,</span><span class="holder-role">Business Owner</span></p>
  <ul class="contact-list">
    <li><svg class="contact-icon" viewBox="0 0 12 12"><circle cx="6" cy="6" r="5.5" fill="var(--brand-red)"/><path d="M4,3 L5,5 L4.5,6 Q5.5,7.5 7,8 L8,7.5 L9,8.5 Q8,10 6.5,9.5 Q3.5,8 2.8,4.5 Q3,3.2 4,3Z" fill="#fff"/></svg>0438519627</li>
    <li><svg class="contact-icon" viewBox="0 0 12 12"><circle cx="6" cy="6" r="5.5" fill="var(--brand-red)"/><rect x="3" y="4" width="6" height="4.2" fill="#fff"/><path d="M3,4 L6,6.3 L9,4" stroke="var(--brand-red)" stroke-width="0.8" fill="none"/></svg>marcusdelane@crestlineventurepartners.com</li>
    <li><svg class="contact-icon" viewBox="0 0 12 12"><circle cx="6" cy="6" r="5.5" fill="var(--brand-red)"/><circle cx="6" cy="6" r="3.3" stroke="#fff" stroke-width="0.8" fill="none"/><path d="M2.7,6 H9.3 M6,2.7 V9.3" stroke="#fff" stroke-width="0.8"/></svg>www.crestlineventurepartners.com.au</li>
  </ul>
  <div class="brand-lockup">
    <p class="brand-name"><span class="brand-dot"></span>Crestline Venture Partners</p>
    <p class="brand-tagline">Providing Effective Project Controls and Management Solutions</p>
  </div>
</section>

<!-- Back 1 -->
<section class="card card--back-1" aria-label="Card back, option one">
  <svg class="card-shape" viewBox="0 0 458 262" preserveAspectRatio="none" aria-hidden="true">
    <rect width="458" height="262" fill="var(--brand-red)"/>
    <path d="M0,0 L272,0 C420,40 470,200 388,262 L0,262 Z" fill="var(--ink)"/>
    <path d="M0,0 L250,0 C400,40 448,200 368,262 L0,262 Z" fill="var(--paper)"/>
  </svg>
  <ul class="values"><li>PROVIDING</li><li>KNOWLEDGE</li><li>EXPERTISE</li><li>EXPERIENCE</li></ul>
  <p class="back-mark">Crestline<br>Venture<br>Partners</p>
</section>

<!-- Back 2 -->
<section class="card card--back-2" aria-label="Card back, option two">
  <p class="back-mark">Crestline<br>Venture<br>Partners</p>
  <ul class="values"><li>PROVIDING</li><li>KNOWLEDGE</li><li>EXPERTISE</li><li>EXPERIENCE</li></ul>
</section>

<!-- Back 3 -->
<section class="card card--back-3" aria-label="Card back, option three">
  <p class="back-mark">Crestline<br>Venture<br>Partners</p>
  <ul class="values"><li>PROVIDING</li><li>KNOWLEDGE</li><li>EXPERTISE</li><li>EXPERIENCE</li></ul>
</section>

</body>
</html>
```